Pelmora Tours - Astronomy in the Kimberley

Pelmora Tours requires a web page to advertise astronomy tours in the East Kimberley, Australia. It needs the following tabs - Home, Tours, Astronomy Events, Gallery, Testimonials, Contacts.

It should target tourists to the Kimberley.
We are unsure of which colours to go with at the moment but we have included our logo if it helps.

It should be mobile and tablet friendly.

Target Market(s)

Families, +40, Tourist, hobby astronomists,

Industry/Entity Type

Events

Number of Pages Required

3 page

Colors
3377b5
ffffff

Requirements
Must have
• Home, Tours, Astronomy Events, Gallery, Calendar, Testimonials, Contacts.
• 'Pelmora Tours' logo
Nice to have
• Pictures of portable amateur telescopes. Pictures of Lake Kununurra or Wyndham.
Should not have
• Pictures of extremely large professional telescopes.

```html
<!DOCTYPE html>
<html lang="en">
<head>
<meta charset="utf-8">
<title>Pelmora Tours - Astronomy in the Kimberley</title>
<link rel="stylesheet" href="https://fonts.googleapis.com/css2?family=Exo:wght@300;400;500;600;700&family=Open+Sans:wght@400;600;700&display=swap">
<style>
:root{
  --blue:#2c5fae;
  --blue-bright:#3377b5;
  --blue-band:#2f67b8;
  --blue-soft:#8fc3e8;
  --navy:#0b1a3a;
  --ink:#2a2a2a;
  --grey-text:#8a8a8a;
  --grey-bg:#ececec;
  --card-bg:#f5f5f5;
  --dark:#1b1b1b;
  --dark-field:#3a3a3a;
  --dark-btn:#2f2f2f;
  --white:#ffffff;
  --social-a:#4b4fa0;
  --social-b:#55a9d8;
  --social-c:#e9553d;
}
*{margin:0;padding:0;box-sizing:border-box}
html,body{width:1200px;height:2735px;overflow:hidden}
body{font-family:"Open Sans",Arial,sans-serif;color:var(--ink);background:var(--white);position:relative}
.abs{position:absolute}
.head{font-family:"Exo",Arial,sans-serif}

/* hero */
.hero{position:absolute;left:0;top:0;width:1200px;height:801px;overflow:hidden}
.hero-photo{position:absolute;inset:0;background:linear-gradient(180deg,#0a1633 0%,#13264f 40%,#243357 62%,#3a3430 82%,#2a211b 100%)}
.topbar-link{top:30px;font-size:13px;color:#b9c3d6;font-family:"Exo",sans-serif}
.topline{left:172px;width:856px;height:1px;background:rgba(255,255,255,.18)}
.social-sq{top:26px;width:24px;height:24px;border:1px solid rgba(255,255,255,.25)}
.nav a{position:absolute;top:134px;font-family:"Exo",sans-serif;font-size:14px;font-weight:500;color:var(--white);text-decoration:none;white-space:nowrap}
.nav .active{border-bottom:0}
.nav-active-line{left:172px;top:170px;width:62px;height:3px;background:var(--blue-bright)}
.logo{left:518px;top:62px;width:164px;height:164px;border-radius:50%;background:#081228;border:3px solid rgba(255,255,255,.85);display:flex;align-items:center;justify-content:center;flex-direction:column}
.logo span{font-family:"Exo",sans-serif;font-weight:600;color:var(--white);font-size:26px;line-height:1.05;text-align:center}
.hero-title{left:0;width:1200px;top:298px;text-align:center;font-family:"Exo",sans-serif;font-weight:600;font-size:54px;color:var(--white)}
.hero-sub{left:0;width:1200px;top:362px;text-align:center;font-family:"Exo",sans-serif;font-weight:300;font-size:46px;color:var(--white)}
.hero-rule{left:550px;top:438px;width:100px;height:2px;background:var(--blue-bright)}
.callbar{left:365px;top:495px;width:330px;height:59px;background:rgba(10,18,40,.55);display:flex;align-items:center}
.callbar .lbl{font-size:13px;color:var(--white);padding-left:28px;width:212px}
.callbar .ico{width:56px;height:59px;background:var(--blue);display:flex;align-items:center;justify-content:center}
.call-num{left:712px;top:510px;font-family:"Exo",sans-serif;font-size:19px;font-weight:600;color:var(--white)}
.btn{display:flex;align-items:center;justify-content:center;font-family:"Exo",sans-serif;font-weight:700;color:var(--white);text-transform:uppercase}
.btn-reach{left:502px;top:613px;width:193px;height:59px;background:var(--blue);font-size:13px}
.arrow{width:54px;height:54px;border-radius:50%;border:2px solid rgba(255,255,255,.7);background:rgba(0,0,0,.35);display:flex;align-items:center;justify-content:center;top:371px}
.dot{top:749px;width:7px;height:7px;border-radius:50%;border:1px solid #fff}

/* welcome */
.welcome-title{left:0;width:1200px;top:852px;text-align:center;font-family:"Exo",sans-serif;font-size:31px;font-weight:300;color:var(--ink);letter-spacing:1px}
.welcome-title b{font-weight:600}
.welcome-rule{left:556px;top:907px;width:88px;height:2px;background:var(--blue-soft)}
.welcome-sub{left:0;width:1200px;top:924px;text-align:center;font-size:12px;color:var(--blue-soft)}
.card{top:1032px;width:210px;height:189px;background:var(--card-bg);text-align:center}
.card-icon{position:absolute;left:61px;top:-50px;width:88px;height:88px;border-radius:50%;background:var(--blue);border:4px solid #dce6f4;display:flex;align-items:center;justify-content:center}
.card h3{position:absolute;left:0;width:100%;top:63px;font-family:"Exo",sans-serif;font-size:13px;font-weight:700;color:var(--ink)}
.card p{position:absolute;left:18px;width:174px;top:92px;font-size:10.5px;line-height:14px;color:var(--grey-text)}
.card .more{position:absolute;left:59px;top:158px;width:92px;height:31px;background:var(--blue);font-size:11px}
.btn-services{left:502px;top:1268px;width:196px;height:59px;background:var(--dark-btn);font-size:13px}

/* caravan */
.feature-grey{left:0;top:1374px;width:1200px;height:436px;background:var(--grey-bg)}
.feature-blue{left:0;top:1810px;width:1200px;height:288px;background:var(--blue-band)}
.feature-kicker{left:0;width:1200px;top:1432px;text-align:center;font-family:"Exo",sans-serif;font-weight:300;font-size:31px;color:#9a9a9a;letter-spacing:1px}
.feature-rule{left:556px;top:1480px;width:88px;height:1px;background:#bdbdbd}
.feature-title{left:0;width:1200px;top:1484px;text-align:center;font-family:"Exo",sans-serif;font-weight:400;font-size:40px;color:var(--blue)}
.caravan{left:224px;top:1591px;width:719px;height:271px;border-radius:60px 110px 20px 20px;background:linear-gradient(180deg,#fbfbfb 0%,#e9eaec 70%,#cfd1d4 100%)}
.feature-text{left:235px;width:730px;top:1888px;text-align:center;font-size:12.5px;line-height:19px;color:var(--white)}
.btn-book{left:502px;top:1975px;width:193px;height:57px;background:#21375d;font-size:13px}

/* contact strip */
.strip-col{top:2136px}
.strip-col h4{font-family:"Exo",sans-serif;font-size:16px;font-weight:500;color:var(--ink)}
.strip-val{display:flex;align-items:center;gap:10px;margin-top:10px;font-family:"Exo",sans-serif;font-size:21px;color:var(--blue)}
.strip-col small{display:block;margin-top:4px;padding-left:34px;font-size:11px;color:var(--ink)}
.strip-div{top:2140px;width:1px;height:70px;background:#dcdcdc}

/* footer */
.footer{left:0;top:2251px;width:1200px;height:412px;background:var(--dark)}
.f-head{top:2314px;font-family:"Exo",sans-serif;font-size:12px;font-weight:600;color:#cfcfcf;letter-spacing:.5px}
.field{background:var(--dark-field);font-size:11px;color:#9a9a9a;padding:8px 10px}
.btn-send{left:172px;top:2477px;width:278px;height:31px;background:var(--blue);font-size:11px}
.blog-item{left:511px;width:230px;height:48px}
.blog-thumb{position:absolute;left:0;top:0;width:47px;height:48px;background:linear-gradient(180deg,#0d1d4a,#1f3d7a 60%,#101820);border:1px solid #555}
.blog-item h5{position:absolute;left:60px;top:0;font-family:"Exo",sans-serif;font-size:11px;font-weight:700;color:#dcdcdc}
.blog-item p{position:absolute;left:60px;top:17px;font-size:10px;color:#8a8a8a}
.blog-item span{position:absolute;left:60px;top:32px;font-size:9px;font-weight:700;color:#e0e0e0}
.special{left:778px;top:2352px;width:250px;height:153px;background:linear-gradient(180deg,#3c2a4c 0%,#b8473b 45%,#f08a3a 70%,#2a1a1a 100%)}
.badge{left:938px;top:2352px;width:71px;height:98px;background:var(--blue-soft);clip-path:polygon(0 0,100% 0,100% 100%,50% 82%,0 100%);text-align:center;font-family:"Exo",sans-serif;font-size:12px;font-weight:600;color:#173a66;padding-top:22px;line-height:14px}
.f-rule{left:172px;top:2545px;width:856px;height:1px;background:#333}
.social-bar{top:2576px;height:40px;display:flex;align-items:center;font-family:"Exo",sans-serif;font-size:11px;font-weight:600;color:var(--white);letter-spacing:.5px}
.social-bar .sq{width:40px;height:40px;display:flex;align-items:center;justify-content:center;border-right:1px solid rgba(255,255,255,.3)}
.social-bar .name{flex:1;text-align:center;border-right:1px solid rgba(255,255,255,.3)}
.social-bar .count{width:100px;text-align:center}
.copyright{left:0;width:1200px;top:2690px;display:flex;justify-content:center;align-items:center;gap:14px;font-size:11px;color:#666}
.copyright .mark{width:18px;height:18px;border-radius:50%;background:var(--blue)}
.copyright b{color:var(--ink)}
</style>
</head>
<body>

<!-- HERO -->
<section class="hero">
  <div class="hero-photo" role="img" aria-label="Night sky over the Kimberley with stargazers setting up portable amateur telescopes"></div>
  <a class="abs topbar-link" style="left:180px">Login</a>
  <span class="abs topbar-link" style="left:226px">/</span>
  <a class="abs topbar-link" style="left:246px">Register</a>
  <div class="abs social-sq" style="left:896px"></div>
  <div class="abs social-sq" style="left:932px"></div>
  <div class="abs social-sq" style="left:968px"></div>
  <div class="abs social-sq" style="left:1004px"></div>
  <div class="abs topline" style="top:60px"></div>

  <nav class="nav">
    <a style="left:184px">Home</a>
    <a style="left:280px">Astronomy Events</a>
    <a style="left:451px">Tours</a>
    <a style="left:713px">Gallery</a>
    <a style="left:818px">Testimonials</a>
    <a style="left:953px">Contacts</a>
  </nav>
  <div class="abs topline" style="top:172px"></div>
  <div class="abs nav-active-line"></div>

  <div class="abs logo"><span>Pelmora<br>Tours</span></div>

  <h1 class="abs hero-title">Travel With Us For The Best Deal !</h1>
  <p class="abs hero-sub">Enjoy Wonderful Feelings !</p>
  <div class="abs hero-rule"></div>

  <div class="abs callbar">
    <span class="lbl">Any Questions? Call Us:</span>
    <span class="ico">
      <svg width="22" height="22" viewBox="0 0 24 24"><path fill="#fff" d="M6.6 10.8a15 15 0 0 0 6.6 6.6l2.2-2.2c.3-.3.7-.4 1-.2 1.1.4 2.3.6 3.6.6.6 0 1 .4 1 1V20c0 .6-.4 1-1 1A17 17 0 0 1 3 4c0-.6.4-1 1-1h3.5c.6 0 1 .4 1 1 0 1.3.2 2.5.6 3.6.1.3 0 .7-.2 1z"/></svg>
    </span>
  </div>
  <div class="abs call-num">0800 (555) 0147</div>

  <a class="abs btn btn-reach">Reach us today</a>

  <div class="abs arrow" style="left:58px"><svg width="14" height="14" viewBox="0 0 14 14"><path d="M9 2 4 7l5 5" fill="none" stroke="#fff" stroke-width="2"/></svg></div>
  <div class="abs arrow" style="left:1084px"><svg width="14" height="14" viewBox="0 0 14 14"><path d="m5 2 5 5-5 5" fill="none" stroke="#fff" stroke-width="2"/></svg></div>

  <span class="abs dot" style="left:582px;background:#fff"></span>
  <span class="abs dot" style="left:596px"></span>
  <span class="abs dot" style="left:610px"></span>
</section>

<!-- WELCOME -->
<h2 class="abs welcome-title">WELCOME TO THE <b>PELMORA TOURS</b></h2>
<div class="abs welcome-rule"></div>
<p class="abs welcome-sub">Travel With Us For The Best Deal !</p>

<article class="abs card" style="left:172px">
  <div class="card-icon"><svg width="40" height="40" viewBox="0 0 40 40" fill="none" stroke="#fff" stroke-width="2.5"><path d="M8 20 30 10l3 6-22 10z"/><path d="M20 22l-6 12M20 22l6 12M20 22v12"/></svg></div>
  <h3>PELMORA TOURS</h3>
  <p>Lorem ipsum dolor sit amet, consec adipiscing elit, sed diam nonummy nibh euismod ti themsa me.</p>
  <a class="btn more">More</a>
</article>
<article class="abs card" style="left:386px">
  <div class="card-icon"><svg width="40" height="40" viewBox="0 0 40 40" fill="#fff"><circle cx="20" cy="20" r="8"/><circle cx="8" cy="9" r="2"/><circle cx="32" cy="12" r="1.6"/><circle cx="31" cy="31" r="2"/><circle cx="9" cy="30" r="1.4"/></svg></div>
  <h3>PELMORA TOURS</h3>
  <p>Lorem ipsum dolor sit amet, consec adipiscing elit, sed diam nonummy nibh euismod ti themsa me.</p>
  <a class="btn more">More</a>
</article>
<article class="abs card" style="left:600px">
  <div class="card-icon"><svg width="42" height="40" viewBox="0 0 42 40" fill="none" stroke="#fff" stroke-width="2.5"><rect x="4" y="9" width="30" height="20" rx="5"/><rect x="10" y="14" width="9" height="6" fill="#fff"/><path d="M34 25h6"/><circle cx="15" cy="31" r="3" fill="#2c5fae"/></svg></div>
  <h3>PELMORA TOURS</h3>
  <p>Lorem ipsum dolor sit amet, consec adipiscing elit, sed diam nonummy nibh euismod ti themsa me.</p>
  <a class="btn more">More</a>
</article>
<article class="abs card" style="left:814px">
  <div class="card-icon"><svg width="40" height="40" viewBox="0 0 40 40" fill="none" stroke="#fff" stroke-width="2.5"><circle cx="20" cy="20" r="13"/><path d="M7 20h26M20 7c-6 7-6 19 0 26M20 7c6 7 6 19 0 26"/></svg></div>
  <h3>PELMORA TOURS</h3>
  <p>Lorem ipsum dolor sit amet, consec adipiscing elit, sed diam nonummy nibh euismod ti themsa me.</p>
  <a class="btn more">More</a>
</article>

<a class="abs btn btn-services">See more services</a>

<!-- CARAVAN FEATURE -->
<section>
  <div class="abs feature-grey"></div>
  <div class="abs feature-blue"></div>
  <p class="abs feature-kicker">TOURISTS TO THE KIMBERLEY SUCH AS</p>
  <div class="abs feature-rule"></div>
  <h2 class="abs feature-title">CARAVAN TRAILERS</h2>
  <div class="abs caravan" role="img" aria-label="White touring caravan trailer seen from the side"></div>
  <p class="abs feature-text">Lorem ipsum dolor sit amet, consec adipiscing elit, sed diam nonummy nibh euismod ti themsa me Lorem ipsum dolor sit amet, consec adipiscing elit, sed diam nonummy nibh euismod ti themsa me Lorem ipsum dolor sit amet, consec adipiscing elit, sed diam nonummy nibh euismod ti themsa me.</p>
  <a class="abs btn btn-book">Book now !</a>
</section>

<!-- CONTACT STRIP -->
<div class="abs strip-col" style="left:172px">
  <h4>Book by Phone !</h4>
  <div class="strip-val"><svg width="22" height="22" viewBox="0 0 24 24"><path fill="#2c5fae" d="M6.6 10.8a15 15 0 0 0 6.6 6.6l2.2-2.2c.3-.3.7-.4 1-.2 1.1.4 2.3.6 3.6.6.6 0 1 .4 1 1V20c0 .6-.4 1-1 1A17 17 0 0 1 3 4c0-.6.4-1 1-1h3.5c.6 0 1 .4 1 1 0 1.3.2 2.5.6 3.6.1.3 0 .7-.2 1z"/></svg>1-223-555-0192</div>
  <small>Booking time: 24 / 7 hours !</small>
</div>
<div class="abs strip-div" style="left:420px"></div>
<div class="abs strip-col" style="left:457px">
  <h4>Give your Feedback !</h4>
  <div class="strip-val"><svg width="24" height="22" viewBox="0 0 24 22" fill="none" stroke="#2c5fae" stroke-width="2"><rect x="2" y="4" width="20" height="14"/><path d="m2 4 10 8 10-8"/></svg>hello@pelmoramail.net</div>
  <small>Help us improve!</small>
</div>
<div class="abs strip-div" style="left:738px"></div>
<div class="abs strip-col" style="left:775px">
  <h4>Services and Support !</h4>
  <div class="strip-val"><svg width="22" height="22" viewBox="0 0 24 24" fill="none" stroke="#2c5fae" stroke-width="2"><path d="M4 14v-2a8 8 0 0 1 16 0v2"/><rect x="3" y="13" width="4" height="6" rx="1"/><rect x="17" y="13" width="4" height="6" rx="1"/></svg>Support &amp; Service Centre</div>
  <small>Get your doubts cleared</small>
</div>

<!-- FOOTER -->
<footer>
  <div class="abs footer"></div>

  <h4 class="abs f-head" style="left:172px">CONTACT US</h4>
  <div class="abs field" style="left:172px;top:2355px;width:134px;height:31px">Name</div>
  <div class="abs field" style="left:316px;top:2355px;width:134px;height:31px">Email</div>
  <div class="abs field" style="left:172px;top:2397px;width:278px;height:73px">Message</div>
  <a class="abs btn btn-send">Send</a>

  <h4 class="abs f-head" style="left:511px">BLOG</h4>
  <div class="abs blog-item" style="top:2350px"><div class="blog-thumb" role="img" aria-label="Night sky photo"></div><h5>PELMORA TOURS</h5><p>Lorem ipsum dolor sit amet.</p><span>MORE</span></div>
  <div class="abs blog-item" style="top:2404px"><div class="blog-thumb" role="img" aria-label="Night sky photo"></div><h5>PELMORA TOURS</h5><p>Lorem ipsum dolor sit amet.</p><span>MORE</span></div>
  <div class="abs blog-item" style="top:2458px"><div class="blog-thumb" role="img" aria-label="Night sky photo"></div><h5>PELMORA TOURS</h5><p>Lorem ipsum dolor sit amet.</p><span>MORE</span></div>

  <h4 class="abs f-head" style="left:778px">SPECIAL</h4>
  <div class="abs special" role="img" aria-label="Silhouette of a telescope against an orange sunset sky"></div>
  <div class="abs badge">SPECIAL<br>OFFER<br>!!!</div>

  <div class="abs f-rule"></div>

  <div class="abs social-bar" style="left:172px;width:266px;background:var(--social-a)"><span class="sq"></span><span class="name">FRIENDBOOK</span><span class="count">90k+ LIKES</span></div>
  <div class="abs social-bar" style="left:469px;width:264px;background:var(--social-b)"><span class="sq"></span><span class="name">CHIRPER</span><span class="count">90k+ TWEETS</span></div>
  <div class="abs social-bar" style="left:761px;width:267px;background:var(--social-c)"><span class="sq"></span><span class="name">CIRCLES+</span><span class="count">90k+ PLUS</span></div>

  <div class="abs copyright"><span class="mark"></span><span>Copyrights © <b>Pelmora-Tours</b> 2015. All Rights Reserved. Privacy Policy.</span></div>
</footer>

</body>
</html>
```